Harbor Kindness Inc

We need a full re-design of our non-profit organization website (www.harborkindness.org). Ideally, we are looking to make it more attractive, user-friendly, and interactive with our business model.

Please make sure to user colors that ago with our logo.

We need a homepage done and we also need a content page done where we will use for the other pages to fill with content.

Target Market(s)

Clothes/textiles donations.

Industry/Entity Type

Charity

Number of Pages Required

2 page

Colors

Designer to choose colors to be used in the design.

Requirements
Must have
• It must match the styling of our logo and same colors as current website. (www.harborkindness.org)
Nice to have
• Sleek homepage that is easy to understand and get our main points across.

```html
<!DOCTYPE html>
<html lang="en">
<head>
<meta charset="utf-8">
<title>Harbor Kindness</title>
<link rel="stylesheet" href="https://fonts.googleapis.com/css2?family=Montserrat:wght@400;500;600;700&family=Open+Sans:wght@400;600;700&display=swap">
<style>
:root{
  --black:#141414;
  --white:#ffffff;
  --green:#4e8a2e;
  --green-light:#6cbf3f;
  --green-text:#3f7f1f;
  --red:#e1252d;
  --yellow:#f7c400;
  --paper:#f3f2ee;
  --ink:#1b1b1b;
  --muted:#8a8a8a;
  --band:#454545;
  --footer:#333333;
  --bottom:#1f1f1f;
}
*{box-sizing:border-box;margin:0;padding:0}
html,body{width:1200px;height:2769px;overflow:hidden}
body{font-family:"Open Sans",Arial,sans-serif;color:var(--ink);background:var(--white);position:relative}
section,header,footer,nav{position:relative;width:1200px}
.abs{position:absolute}

.topbar{height:72px;background:var(--black)}
.brand{left:162px;top:18px;display:flex;align-items:center;gap:10px}
.brand-mark{width:34px;height:34px;background:var(--yellow)}
.brand-name{font-family:"Montserrat",Arial,sans-serif;font-weight:700;font-size:18px;color:var(--white)}
.social{left:692px;top:20px;display:flex;gap:8px}
.social span{width:30px;height:30px;border-radius:50%;display:block}
.btn-top{left:951px;top:20px;width:87px;height:32px;background:var(--green-light);color:var(--white);font-size:11px;font-weight:700;display:flex;align-items:center;justify-content:center;border-radius:2px}

.nav{height:46px;background:var(--white);border-bottom:1px solid #e6e6e6}
.nav a{position:absolute;top:16px;font-family:"Montserrat",Arial,sans-serif;font-size:12px;font-weight:700;color:var(--ink);text-decoration:none}
.nav a.active{color:var(--green-light)}

.hero{height:500px;overflow:hidden}
.hero-photo{left:0;top:0;width:1200px;height:500px;background:linear-gradient(90deg,#d9d3c6 0%,#ece9e2 35%,#f7f6f3 60%,#fbfbfa 100%)}
.hero-box{left:75px;top:90px;width:560px;height:330px;background:linear-gradient(180deg,#b9b3aa 0%,#c8a77b 40%,#c89a62 100%);border-radius:6px}
.hero-title{left:733px;top:232px;font-family:"Montserrat",Arial,sans-serif;font-weight:600;font-size:70px;line-height:80px;color:var(--black)}
.btn{display:flex;align-items:center;justify-content:center;gap:12px;color:var(--white);font-weight:600;font-family:"Open Sans",Arial,sans-serif;border-radius:2px}
.btn svg{width:22px;height:22px}
.btn-red{left:733px;top:432px;width:264px;height:59px;background:var(--red);font-size:14px}

.how{height:595px;background:var(--paper);text-align:center}
.section-title{width:100%;font-family:"Montserrat",Arial,sans-serif;font-weight:600;font-size:26px;color:var(--black);text-align:center}
.section-sub{width:100%;font-size:19px;text-align:center;color:var(--ink)}
.step{width:260px;text-align:center}
.step-icon{margin:0 auto;width:74px;height:74px;border-radius:8px;background:#e4e1da}
.step h3{margin-top:30px;font-size:14px;font-weight:600;line-height:21px;color:var(--green-text)}
.step p{margin-top:10px;font-size:11px;line-height:15px;color:var(--muted)}
.btn-green{left:493px;top:451px;width:214px;height:59px;background:var(--green);font-size:14px}

.donation{height:439px;background:var(--white)}
.card{width:192px}
.card-head{display:flex;align-items:center;gap:12px}
.card-mark{width:38px;height:34px;background:var(--yellow)}
.card-head h4{font-size:11px;font-weight:700;color:var(--green-text)}
.meter{margin-top:14px;height:52px;background:var(--green-light);border-radius:3px;padding:7px 9px;color:var(--white)}
.meter-track{height:10px;background:#fff;border-radius:5px;overflow:hidden}
.meter-fill{height:10px;width:80%;background:var(--black)}
.meter-row{display:flex;justify-content:space-between;font-size:10px;font-weight:700;margin-top:4px}
.meter-row.small{font-size:7px;font-weight:400;margin-top:1px}
.card-meta{margin-top:14px;font-size:10px;color:var(--muted);line-height:17px}
.card-meta b{color:var(--ink)}
.card-desc{margin-top:8px;font-size:10px;color:var(--muted);line-height:16px}

.mission{height:606px;background:radial-gradient(ellipse at 30% 55%,#5a5450 0%,#2c2a28 45%,#141414 80%)}
.mission-photo{left:0;top:0;width:720px;height:606px;background:radial-gradient(ellipse at 55% 58%,#6b6158 0%,#3a3532 40%,rgba(20,20,20,0) 75%)}
.play{left:416px;top:282px}
.mission-kicker{left:746px;top:114px;font-family:"Montserrat",Arial,sans-serif;font-weight:600;font-size:30px;line-height:40px;color:var(--white);white-space:nowrap}
.mission-title{left:746px;top:162px;font-family:"Montserrat",Arial,sans-serif;font-weight:600;font-size:42px;line-height:53px;color:var(--white);white-space:nowrap}
.mission-text{left:746px;top:284px;width:300px;font-size:12.5px;line-height:18px;color:var(--white)}
.btn-mission{left:746px;top:408px;width:171px;height:44px;background:var(--green-light);font-size:13px}

.finder{height:101px;background:var(--band)}
.finder h2{left:162px;top:34px;font-family:"Montserrat",Arial,sans-serif;font-weight:600;font-size:24px;color:var(--white)}
.input{background:var(--white);border-radius:2px;font-size:10px;color:#777;padding-left:22px;display:flex;align-items:center}
.finder .input{left:502px;top:31px;width:434px;height:37px}
.btn-yellow{left:941px;top:31px;width:98px;height:37px;background:var(--yellow);color:var(--white);font-size:14px;font-weight:700;display:flex;align-items:center;justify-content:center}

.footer{height:336px;background:var(--footer);color:var(--white)}
.foot-mark{left:185px;top:35px;width:100px;height:84px;background:var(--yellow)}
.foot-name{left:162px;top:142px;font-family:"Montserrat",Arial,sans-serif;font-weight:700;font-size:17px}
.foot-text{left:162px;top:190px;width:400px;font-size:11px;line-height:17px;color:#9a9a9a}
.foot-text p+p{margin-top:12px}
.sponsors-title{left:681px;top:44px;font-family:"Montserrat",Arial,sans-serif;font-weight:600;font-size:19px}
.sponsors{left:681px;top:87px;display:flex;gap:10px}
.sponsors span{width:60px;height:60px;background:#e8df7a;display:block}
.sponsors span.round{border-radius:50%;background:#e3b521}
.footer .input{left:681px;top:183px;width:253px;height:33px}
.btn-sub{left:940px;top:183px;width:99px;height:33px;background:var(--green-light);font-size:12px;font-weight:700;display:flex;align-items:center;justify-content:center}
.foot-social{left:681px;top:254px;display:flex;gap:26px}
.foot-social span{width:18px;height:18px;border-radius:50%;background:#777;display:block}

.copyright{height:74px;background:var(--bottom);color:#9a9a9a;font-size:11px;text-align:center;line-height:74px}
</style>
</head>
<body>

<header class="topbar">
  <div class="abs brand"><span class="brand-mark"></span><span class="brand-name">Harbor Kindness</span></div>
  <div class="abs social" aria-label="Social links">
    <span style="background:#3aa1e0"></span><span style="background:#3b5998"></span><span style="background:#1ab7ea"></span><span style="background:#e62117"></span><span style="background:#cb2027"></span><span style="background:#dd4b39"></span>
  </div>
  <div class="abs btn-top">DONATE</div>
</header>

<nav class="nav">
  <a class="active" style="left:162px">HOME</a>
  <a style="left:242px">MISSIONS »</a>
  <a style="left:351px">HOW IT WORKS</a>
  <a style="left:482px">ABOUT US »</a>
  <a style="left:593px">SPONSORS</a>
  <a style="left:701px">NEWS</a>
  <a style="left:781px">DONATE</a>
  <a style="left:871px">WALL OF NEEDS</a>
  <svg class="abs" style="left:1022px;top:15px" width="16" height="16" viewBox="0 0 16 16"><circle cx="6.5" cy="6.5" r="4.5" fill="none" stroke="#6cbf3f" stroke-width="2"/><line x1="10" y1="10" x2="14" y2="14" stroke="#6cbf3f" stroke-width="2"/></svg>
</nav>

<section class="hero">
  <div class="abs hero-photo" role="img" aria-label="Cardboard donation box filled with folded clothes on a light wooden table"></div>
  <div class="abs hero-box" role="img" aria-label="Open cardboard box of donated sweaters"></div>
  <h1 class="abs hero-title">Harbor<br>Kindness</h1>
  <div class="abs btn btn-red">More About Harbor Kindness
    <svg viewBox="0 0 22 22"><circle cx="11" cy="11" r="10" fill="#fff"/><path d="M6 11h9M11 7l4 4-4 4" stroke="#e1252d" stroke-width="2.2" fill="none"/></svg>
  </div>
</section>

<section class="how">
  <h2 class="abs section-title" style="top:76px">HOW IT WORKS</h2>
  <p class="abs section-sub" style="top:124px">We have different collection procedures. For outdoors we can place a donation bin,</p>
  <div class="abs step" style="left:156px;top:194px">
    <div class="step-icon" role="img" aria-label="Dress in a donation basket"></div>
    <h3>Drop off clothing at your<br>closest donation bin.</h3>
    <p>We have different collection procedures. For outdoors we can place a donation bin, a metal container about 4ft L X 4ftW X6ft H.</p>
  </div>
  <div class="abs step" style="left:470px;top:194px">
    <div class="step-icon" role="img" aria-label="Driver carrying a bag of clothes"></div>
    <h3>We pick it up and take it to<br>our sorting facility</h3>
    <p>After our drivers pick up the clothing from our designated donation locations, the items are taken to our sorting facility where they are separated...</p>
  </div>
  <div class="abs step" style="left:780px;top:194px">
    <div class="step-icon" role="img" aria-label="T-shirt with a heart"></div>
    <h3>Charities get clothing. We<br>pay you for the clothes.</h3>
    <p>Once we are done distributing our donated clothing to their appropriate channels, the proceeds from the sales are distributed in two ways.</p>
  </div>
  <div class="abs btn btn-green">Learn How It Works
    <svg viewBox="0 0 22 22"><circle cx="11" cy="11" r="10" fill="#fff"/><path d="M6 11h9M11 7l4 4-4 4" stroke="#4e8a2e" stroke-width="2.2" fill="none"/></svg>
  </div>
</section>

<section class="donation">
  <h2 class="abs section-title" style="top:62px">Donation</h2>
  <p class="abs section-sub" style="top:110px">If you are looking to make a financial donation in the form of a check,</p>
  <article class="abs card" style="left:162px;top:190px">
    <div class="card-head"><span class="card-mark"></span><h4>EASTFIELD LETTER</h4></div>
    <div class="meter"><div class="meter-track"><div class="meter-fill"></div></div><div class="meter-row"><span>$10,000</span><span>$25,000</span></div><div class="meter-row small"><span>START</span><span>END</span></div></div>
    <div class="card-meta">June 4, 2016 Categories :<br><b>MAIN</b> by <b>ADMIN</b></div>
    <p class="card-desc">May 25, 2015: Donated clothes to Eastfield Employee Service Team of NY.</p>
  </article>
  <article class="abs card" style="left:390px;top:190px">
    <div class="card-head"><span class="card-mark"></span><h4>EASTFIELD LETTER</h4></div>
    <div class="meter"><div class="meter-track"><div class="meter-fill"></div></div><div class="meter-row"><span>$10,000</span><span>$25,000</span></div><div class="meter-row small"><span>START</span><span>END</span></div></div>
    <div class="card-meta">June 4, 2016 Categories :<br><b>MAIN</b> by <b>ADMIN</b></div>
    <p class="card-desc">May 25, 2015: Donated clothes to Eastfield Employee Service Team of NY.</p>
  </article>
  <article class="abs card" style="left:618px;top:190px">
    <div class="card-head"><span class="card-mark"></span><h4>EASTFIELD LETTER</h4></div>
    <div class="meter"><div class="meter-track"><div class="meter-fill"></div></div><div class="meter-row"><span>$10,000</span><span>$25,000</span></div><div class="meter-row small"><span>START</span><span>END</span></div></div>
    <div class="card-meta">June 4, 2016 Categories :<br><b>MAIN</b> by <b>ADMIN</b></div>
    <p class="card-desc">May 25, 2015: Donated clothes to Eastfield Employee Service Team of NY.</p>
  </article>
  <article class="abs card" style="left:847px;top:190px">
    <div class="card-head"><span class="card-mark"></span><h4>EASTFIELD LETTER</h4></div>
    <div class="meter"><div class="meter-track"><div class="meter-fill"></div></div><div class="meter-row"><span>$10,000</span><span>$25,000</span></div><div class="meter-row small"><span>START</span><span>END</span></div></div>
    <div class="card-meta">June 4, 2016 Categories :<br><b>MAIN</b> by <b>ADMIN</b></div>
    <p class="card-desc">May 25, 2015: Donated clothes to Eastfield Employee Service Team of NY.</p>
  </article>
</section>

<section class="mission">
  <div class="abs mission-photo" role="img" aria-label="Open cupped hands held out in low light"></div>
  <svg class="abs play" width="40" height="44" viewBox="0 0 40 44"><path d="M4 2l34 20L4 42z" fill="#fff"/></svg>
  <div class="abs mission-kicker">HARBOR KINDNESS</div>
  <div class="abs mission-title">MISSION<br>STATEMENT</div>
  <p class="abs mission-text">Harbor Kindness has a two part mission to help local communities while helping the planet. The average American discards 68 lbs of clothing annually. That is 1,325,340,196 lbs for New York State alone and 21,202,400,000 lbs for the U.S.</p>
  <div class="abs btn btn-mission">Donate Now
    <svg viewBox="0 0 22 22"><circle cx="11" cy="11" r="10" fill="#fff"/><path d="M6 11h9M11 7l4 4-4 4" stroke="#6cbf3f" stroke-width="2.2" fill="none"/></svg>
  </div>
</section>

<section class="finder">
  <h2 class="abs">Find Local Donation Place</h2>
  <div class="abs input">Enter Your Email</div>
  <div class="abs btn-yellow">Search</div>
</section>

<footer class="footer">
  <div class="abs foot-mark"></div>
  <div class="abs foot-name">HARBOR KINDNESS</div>
  <div class="abs foot-text">
    <p>Harbor Kindness is a non-profit organization that was created for one purpose: helping the less fortunate in our country's time of greatest need. Started in 2007, Harbor Kindness has been a dedicated member of its local communities over the past four years.</p>
    <p>The company's clothing collection efforts have allowed it to provide some of the neediest members of the community to clothe themselves and their</p>
  </div>
  <div class="abs sponsors-title">Our Sponsors</div>
  <div class="abs sponsors"><span></span><span></span><span></span><span class="round"></span></div>
  <div class="abs input">Enter Your Email</div>
  <div class="abs btn-sub">SUBSCRIBE</div>
  <div class="abs foot-social"><span></span><span></span><span></span><span></span></div>
</footer>

<div class="copyright">© Copyright 2018 Harbor Kindness. All Rights Reserved.</div>

</body>
</html>
```